Banner for a program to be used as a cover photo for Facebook

Banner design for a program I run called: The Craft of Bold Ascent
This is a 90 day implementation program for business owners who set one main goal to reach during that time. The focus of the program is to help them set the goal, create the strategy to reach the goal and take keystone actions to achieve the goal. This program (I run multiple at a time) is exclusive to only 8 people at a time...the price point of the program is $6,000.

Company Name: Lantern Harbor

My title: Enterprise Momentum Coach (EMC!)

My area of expertise: Helping business owners who already know what they do, who they serve, and have momentum (and sales) accelerate the growth of their business by eliminate what they don't need and simplifying the strategy to achieve mind blowing results. (Success habits, behaviors, routines, attitudes, speed of implementation, simplification, essentialism, focus, goal setting, high performance)

Who I want to attract: People who have made $25k - $75k in the last 12 months of their business (service based) who are action takers, big thinkers, in it to win it, take action even in the face of fear, committed, decision makers

Target Market(s)

Women business owners who have been in business for 2 - 5 years making at least $25k - $75k in their previous 12 months. They are feminine, married, moms, higher end and looking for a more exclusive and selective group of like-minded people to grow with. They are attracted to a more glamorous, boutique feel and desire to catapult the results in their business.

Industry/Entity Type

Business

Font styles to use
Sans Serif

Requirements
Must have
• Crisp, Clean, High End, Simple, Elegant, Picture of me
• Text on Banner:
• The Craft of Bold Ascent
• with Carla Voss, Enterprise Momentum Coach
Should not have
• Men in suits in pictures.
• Corporate Feel.

```html
<!DOCTYPE html>
<html lang="en">
<head>
<meta charset="utf-8">
<title>The Craft of Bold Ascent – Carla Voss</title>
<link rel="stylesheet" href="https://fonts.googleapis.com/css2?family=Montserrat:wght@800&family=Open+Sans:wght@500;700&display=swap">
<style>
  :root {
    --navy: #2b3a97;
    --sky: #35a9e6;
    --slate-violet: #5a5aa8;
    --ink: #2a1f1a;
    --panel: rgba(176, 146, 128, 0.72);
    --panel-edge: rgba(255, 255, 255, 0.75);
    --sea-light: #dfe6ea;
    --sea-mid: #b9c3c8;
    --stone-dark: #4c4640;
    --stone-warm: #8b7a6c;
    --logo: #2f9ee0;
  }
  * { margin: 0; padding: 0; box-sizing: border-box; }
  html, body { width: 1200px; height: 496px; overflow: hidden; background: #fff; }
  .banner {
    position: relative;
    width: 1200px;
    height: 496px;
    overflow: hidden;
    font-family: "Open Sans", Arial, sans-serif;
  }
  .backdrop {
    position: absolute; inset: 0;
    background:
      radial-gradient(ellipse 420px 300px at 930px 330px, rgba(76,70,64,0.85), transparent 70%),
      radial-gradient(ellipse 500px 160px at 700px 470px, rgba(110,96,84,0.9), transparent 75%),
      linear-gradient(180deg, var(--sea-light) 0%, var(--sea-mid) 45%, var(--stone-warm) 80%, var(--stone-dark) 100%);
  }
  .portrait {
    position: absolute;
    left: 20px; top: 40px;
    width: 370px; height: 456px;
    border-radius: 180px 180px 0 0;
    background:
      radial-gradient(ellipse 130px 170px at 170px 170px, #f1d9b8, transparent 72%),
      linear-gradient(180deg, #e4c98f 0%, #efe3cf 55%, #ffffff 80%);
    opacity: 0.95;
  }
  .headline {
    position: absolute;
    left: 140px; top: 14px; width: 820px;
    text-align: center;
    font-family: "Montserrat", Arial, sans-serif;
    font-weight: 800;
    font-size: 40px;
    letter-spacing: 0.2px;
    color: var(--navy);
    line-height: 50px;
  }
  .byline {
    position: absolute;
    left: 205px; top: 62px;
    font-family: "Open Sans", Arial, sans-serif;
    font-weight: 700;
    font-size: 26px;
    line-height: 34px;
    white-space: nowrap;
  }
  .byline .with { color: var(--navy); font-size: 22px; }
  .byline .coach { color: var(--sky); }
  .promise {
    position: absolute;
    left: 368px; top: 135px; width: 360px;
    font-weight: 500;
    font-size: 23px;
    line-height: 30px;
    color: var(--slate-violet);
  }
  .audience {
    position: absolute;
    left: 298px; top: 250px;
    width: 690px; height: 77px;
    border-radius: 12px;
    border: 1px solid var(--panel-edge);
    background: var(--panel);
    display: flex; align-items: center; justify-content: center;
    text-align: center;
    font-weight: 700;
    font-size: 16.5px;
    line-height: 25px;
    color: var(--ink);
    padding: 0 18px;
  }
  .brand {
    position: absolute;
    right: 36px; top: 392px;
    display: flex; align-items: center; gap: 8px;
    font-family: "Open Sans", Arial, sans-serif;
    font-weight: 700;
    font-size: 19px;
    letter-spacing: 1px;
    color: var(--logo);
  }
  .brand-mark { width: 14px; height: 14px; background: var(--logo); }
</style>
</head>
<body>
  <div class="banner">
    <div class="backdrop" role="img" aria-label="Photograph of stacked pebble cairns on a driftwood log by a misty sea shore"></div>
    <div class="portrait" role="img" aria-label="Portrait photograph of Carla Voss, smiling, with shoulder-length blonde hair and a white top"></div>

    <h1 class="headline">Discover the Craft of Bold Ascent</h1>
    <p class="byline"><span class="with">with</span> <span class="coach">Carla Voss, Enterprise Momentum Coach</span></p>

    <p class="promise">Take your Business to the Next Level with our 90-Day Plan for Explosive Growth</p>

    <div class="audience">Designed for women business owners who already know what they do but need to simplify the strategy to achieve mind blowing results.</div>

    <div class="brand"><span class="brand-mark"></span><span>LANTERN HARBOR</span></div>
  </div>
</body>
</html>
```